Website for "Grupo de Tecnicas Renovadas"

We need a new web design for an enterprise dedicated to environment and energy saving engineering, based in Monterrey, Mexico.
They offer consulting services, mainly to enhance building designs, and they are also resellers for several products in the energy saving field.

The final design should be oriented to engineers and architects, and should communicate professionalism, innovation, environment care.

Here is the website of a partner enterprise, which does pretty much the same:

http://www.vientoclaro.example/

Target Market(s)

mainly architects and engineers looking for solutions on energy efficiency building

Industry/Entity Type

Environment

Requirements
Must have
• Entry page must be quite graphical and intuitive, must have a "products listing" and a "projects portfolio".

```html
<!DOCTYPE html>
<html lang="en">
<head>
<meta charset="utf-8">
<title>Grupo de Tecnicas Renovadas</title>
<link rel="stylesheet" href="https://fonts.googleapis.com/css2?family=Oswald:wght@400;500&family=PT+Sans:wght@400;700&display=swap">
<style>
  :root {
    --green: #2aae5e;
    --green-light: #36c274;
    --green-line: #229a50;
    --navy: #12112e;
    --navy-soft: #1c1b3d;
    --white: #ffffff;
    --ink: #1b1b2a;
    --grey-text: #d8d8e4;
  }
  * { margin: 0; padding: 0; box-sizing: border-box; }
  html, body { width: 1200px; height: 2353px; overflow: hidden; background: var(--white); }
  body { position: relative; font-family: "PT Sans", sans-serif; color: var(--ink); }
  .abs { position: absolute; }

  /* Brand */
  .brand { left: 0; top: 96px; width: 1200px; display: flex; justify-content: center; align-items: center; gap: 18px; }
  .brand-dot { width: 58px; height: 58px; border-radius: 50%; background: var(--green); }
  .brand-name { font-family: "Oswald", sans-serif; font-weight: 500; font-size: 42px; color: #4a4a52; letter-spacing: 0.5px; }

  /* Navigation */
  .main-nav { left: 59px; top: 259px; width: 1082px; height: 70px; background: var(--green); display: flex; }
  .main-nav .nav-search { width: 69px; display: flex; align-items: center; justify-content: center; border-right: 1px solid var(--green-line); }
  .main-nav a { flex: 1; display: flex; align-items: center; justify-content: center; color: var(--white); text-decoration: none; font-size: 17px; text-transform: uppercase; border-right: 1px solid var(--green-line); }
  .main-nav a:last-child { border-right: none; }
  .main-nav a.is-active { background: var(--green-light); }

  /* Hero */
  .hero { left: 59px; top: 343px; width: 1082px; height: 349px; }
  .hero-photo { width: 100%; height: 100%; background: linear-gradient(180deg, #c9d3d6 0%, #9fb1a2 35%, #7d8f6c 60%, #5e6d62 100%); }
  .hero-date { left: 0; top: 0; height: 39px; display: flex; }
  .hero-date .date-text { background: var(--green); color: var(--white); font-size: 17px; padding: 0 18px; display: flex; align-items: center; }
  .hero-date .date-icon { background: var(--green-light); width: 45px; display: flex; align-items: center; justify-content: center; }
  .hero-title { left: 0; top: 45px; background: var(--navy); color: var(--white); font-family: "Oswald", sans-serif; font-size: 31px; line-height: 47px; padding: 0 14px; text-transform: uppercase; }
  .hero-arrows { left: 0; bottom: 0; display: flex; gap: 1px; }
  .hero-arrows span { width: 45px; height: 45px; background: var(--navy); display: flex; align-items: center; justify-content: center; }

  /* Section headings */
  .section-heading { left: 59px; font-family: "Oswald", sans-serif; font-weight: 500; font-size: 37px; line-height: 40px; color: var(--green); text-transform: uppercase; }

  /* Products */
  .product-card { top: 747px; width: 353px; height: 351px; }
  .product-photo { width: 100%; height: 100%; }
  .product-title { left: 0; top: 0; background: var(--navy); color: var(--white); font-family: "Oswald", sans-serif; font-size: 31px; line-height: 38px; padding: 2px 14px 4px 16px; text-transform: uppercase; }
  .product-menu { right: 10px; top: 2px; width: 45px; height: 45px; background: var(--navy); display: flex; align-items: center; justify-content: center; }
  .view-more { left: 788px; top: 747px; width: 353px; height: 351px; background: var(--green); color: var(--white); display: flex; align-items: center; justify-content: center; }
  .view-more-text { font-family: "Oswald", sans-serif; font-weight: 500; font-size: 50px; line-height: 54px; text-transform: uppercase; }

  /* News */
  .news-list { left: 59px; top: 1153px; width: 353px; height: 700px; background: var(--navy); }
  .news-tabs { display: flex; height: 47px; }
  .news-tabs span { flex: 1; display: flex; align-items: center; justify-content: center; color: var(--white); font-size: 17px; text-transform: uppercase; }
  .news-tabs .tab-recent { background: var(--green); }
  .news-item { left: 0; width: 353px; height: 123px; background: var(--white); display: flex; }
  .news-thumb { width: 118px; height: 123px; }
  .news-item-title { padding: 18px 12px 0 22px; font-size: 20px; line-height: 27px; color: var(--ink); }
  .news-pointer { right: -14px; top: 46px; width: 0; height: 0; border-top: 16px solid transparent; border-bottom: 16px solid transparent; border-left: 15px solid var(--white); }
  .news-more { left: 0; bottom: 0; width: 353px; height: 127px; background: var(--green); display: flex; align-items: center; justify-content: center; }

  .article { left: 422px; top: 1153px; width: 719px; height: 700px; background: var(--navy); }
  .article-photo { width: 719px; height: 351px; background: linear-gradient(180deg, #8c8aa8 0%, #b7b0c4 45%, #d9cfd6 80%, #c6bfcc 100%); }
  .article-date { right: 0; top: 0; height: 40px; display: flex; }
  .article-date .date-text { background: var(--green); color: var(--white); font-size: 17px; padding: 0 16px; display: flex; align-items: center; }
  .article-date .date-icon { background: var(--green-light); width: 42px; display: flex; align-items: center; justify-content: center; }
  .article-title { left: 24px; top: 380px; color: var(--white); font-size: 28px; font-weight: 700; }
  .article-body { left: 24px; top: 436px; width: 672px; color: var(--grey-text); font-size: 15.5px; line-height: 23.5px; }
  .article-meta { left: 24px; top: 652px; display: flex; align-items: center; gap: 10px; color: var(--white); font-size: 16px; }
  .article-meta .meta-gap { width: 34px; }
  .read-more { right: 24px; top: 650px; color: var(--white); font-size: 18px; font-weight: 700; display: flex; align-items: center; gap: 12px; text-transform: uppercase; }

  /* Footer */
  .footer-band { left: 0; top: 1922px; width: 1200px; height: 68px; background: var(--green); }
  .footer { left: 0; top: 1990px; width: 1200px; height: 363px; background: var(--navy); }
  .about-title { left: 59px; top: 54px; color: var(--white); font-size: 27px; text-transform: uppercase; }
  .about-text { left: 59px; top: 96px; width: 690px; color: var(--white); font-size: 16px; line-height: 20.5px; }
  .about-text p + p { margin-top: 20px; }
  .newsletter { left: 790px; top: 59px; width: 351px; height: 236px; background: var(--green); }
  .newsletter-head { left: 18px; top: 26px; display: flex; align-items: center; gap: 14px; color: var(--white); font-size: 18px; text-transform: uppercase; }
  .newsletter-input { left: 24px; top: 84px; width: 306px; height: 47px; background: var(--white); color: var(--ink); font-size: 16px; padding-left: 20px; display: flex; align-items: center; }
  .newsletter-button { left: 24px; top: 151px; width: 152px; height: 45px; background: var(--green-light); color: var(--white); font-size: 21px; display: flex; align-items: center; justify-content: center; text-transform: uppercase; }
</style>
</head>
<body>

<header class="abs brand">
  <span class="brand-dot"></span>
  <span class="brand-name">Grupo de Tecnicas Renovadas</span>
</header>

<nav class="abs main-nav">
  <span class="nav-search">
    <svg width="22" height="22" viewBox="0 0 22 22"><circle cx="9" cy="9" r="6.5" fill="none" stroke="#fff" stroke-width="3"/><line x1="14" y1="14" x2="20" y2="20" stroke="#fff" stroke-width="3.5" stroke-linecap="round"/></svg>
  </span>
  <a href="#">About</a>
  <a href="#">Products</a>
  <a href="#">Portfolio</a>
  <a href="#" class="is-active">Solutions</a>
  <a href="#">Contact</a>
</nav>

<section class="abs hero">
  <div class="hero-photo" role="img" aria-label="Photo of a circular water treatment plant clarifier with a metal walkway bridge"></div>
  <div class="abs hero-date">
    <span class="date-text">JUNE 2013</span>
    <span class="date-icon"><svg width="22" height="18" viewBox="0 0 22 18"><rect x="1" y="4" width="20" height="13" rx="2" fill="#fff"/><rect x="7" y="1" width="8" height="4" fill="#fff"/><circle cx="11" cy="10.5" r="3.5" fill="#36c274"/></svg></span>
  </div>
  <h1 class="abs hero-title">Water Treatment Plant</h1>
  <div class="abs hero-arrows">
    <span><svg width="12" height="16" viewBox="0 0 12 16"><polyline points="9,2 3,8 9,14" fill="none" stroke="#fff" stroke-width="2.5"/></svg></span>
    <span><svg width="12" height="16" viewBox="0 0 12 16"><polyline points="3,2 9,8 3,14" fill="none" stroke="#fff" stroke-width="2.5"/></svg></span>
  </div>
</section>

<h2 class="abs section-heading" style="top:702px">Products</h2>

<article class="abs product-card" style="left:59px">
  <div class="product-photo" role="img" aria-label="Photo of a solar panel carport structure in a desert parking area" style="background:linear-gradient(180deg,#6d7a8c 0%,#8fa3b4 35%,#a89878 70%,#7e6c50 100%)"></div>
  <h3 class="abs product-title">Solar Array<br>Carport</h3>
  <span class="abs product-menu"><svg width="20" height="16" viewBox="0 0 20 16"><rect y="0" width="20" height="3" fill="#fff"/><rect y="6.5" width="20" height="3" fill="#fff"/><rect y="13" width="20" height="3" fill="#fff"/></svg></span>
</article>

<article class="abs product-card" style="left:424px">
  <div class="product-photo" role="img" aria-label="Photo of an eco friendly office desk with a monitor and desk lamp" style="background:linear-gradient(180deg,#e3d6c6 0%,#c99a6a 45%,#e6e1dc 75%,#b9896a 100%)"></div>
  <h3 class="abs product-title">Eco Friendly<br>Desktop</h3>
  <span class="abs product-menu"><svg width="20" height="16" viewBox="0 0 20 16"><rect y="0" width="20" height="3" fill="#fff"/><rect y="6.5" width="20" height="3" fill="#fff"/><rect y="13" width="20" height="3" fill="#fff"/></svg></span>
</article>

<a class="abs view-more" href="#">
  <span class="view-more-text">View more<br>products
    <svg width="20" height="32" viewBox="0 0 20 32" style="margin-left:6px"><polyline points="5,5 15,16 5,27" fill="none" stroke="#fff" stroke-width="3.5"/></svg>
  </span>
</a>

<h2 class="abs section-heading" style="top:1108px">News</h2>

<aside class="abs news-list">
  <div class="news-tabs">
    <span class="tab-popular">Popular</span>
    <span class="tab-recent">Recent</span>
  </div>
  <div class="abs news-item" style="top:57px">
    <div class="news-thumb" role="img" aria-label="Photo of a power transmission tower" style="background:linear-gradient(180deg,#b9b6c8,#d8d2d8)"></div>
    <p class="news-item-title">US Power Grid Cost Rise</p>
    <span class="abs news-pointer"></span>
  </div>
  <div class="abs news-item" style="top:186px">
    <div class="news-thumb" role="img" aria-label="Photo of lightning striking over a city at night" style="background:linear-gradient(180deg,#3a2a3e,#7e4a3a 60%,#c08a3a)"></div>
    <p class="news-item-title">Thunder struck at Manhattan Street</p>
  </div>
  <div class="abs news-item" style="top:315px">
    <div class="news-thumb" role="img" aria-label="Photo of researchers working in a laboratory" style="background:linear-gradient(180deg,#8a6a5a,#c9b2a2 60%,#e6e0dc)"></div>
    <p class="news-item-title">Scientist research-ing Energy sources in New Guinea</p>
  </div>
  <div class="abs news-item" style="top:444px">
    <div class="news-thumb" role="img" aria-label="Illustration of a glowing blue cell structure" style="background:radial-gradient(circle at 50% 50%,#7aa0e0 0%,#3a5ab0 35%,#0e0e2a 70%)"></div>
    <p class="news-item-title">Power Element</p>
  </div>
  <div class="abs news-more">
    <svg width="32" height="20" viewBox="0 0 32 20"><polyline points="4,4 16,15 28,4" fill="none" stroke="#fff" stroke-width="3.5"/></svg>
  </div>
</aside>

<article class="abs article">
  <div class="article-photo" role="img" aria-label="Photo of a high voltage transmission tower against a pale sky"></div>
  <div class="abs article-date">
    <span class="date-text">24 JULY, 2013</span>
    <span class="date-icon"><svg width="16" height="20" viewBox="0 0 16 20"><rect x="1" y="1" width="14" height="18" fill="#fff"/><rect x="4" y="5" width="8" height="2" fill="#36c274"/><rect x="4" y="9" width="8" height="2" fill="#36c274"/><rect x="4" y="13" width="8" height="2" fill="#36c274"/></svg></span>
  </div>
  <h3 class="abs article-title">US Power Grid Cost Rise</h3>
  <p class="abs article-body">It is a long established fact that a reader will be distracted by the readable content of a page when looking at its layout. The point of using Lorem Ipsum is that it has a more-or-less normal distribution of letters, as opposed to using 'Content here, content here', making it look like readable English. Many desktop publishing packages and web page editors now use Lorem Ipsum as their default model text, and a search for 'lorem ipsum' will uncover many web sites still in their infancy. Various versions have evolved over the years, sometimes by accident, sometimes on purpose (injected humour and the like).</p>
  <div class="abs article-meta">
    <svg width="26" height="16" viewBox="0 0 26 16"><path d="M1 8 Q13 -4 25 8 Q13 20 1 8Z" fill="#fff"/><circle cx="13" cy="8" r="3.5" fill="#12112e"/></svg>
    <span>3,152 views</span>
    <span class="meta-gap"></span>
    <svg width="20" height="18" viewBox="0 0 20 18"><ellipse cx="10" cy="8" rx="9" ry="7" fill="#fff"/><polygon points="4,12 3,18 10,14" fill="#fff"/></svg>
    <span>21 comments</span>
  </div>
  <a class="abs read-more" href="#">Read more
    <svg width="10" height="16" viewBox="0 0 10 16"><polyline points="2,2 8,8 2,14" fill="none" stroke="#2aae5e" stroke-width="2.5"/></svg>
  </a>
</article>

<div class="abs footer-band"></div>
<footer class="abs footer">
  <h4 class="abs about-title">About us</h4>
  <div class="abs about-text">
    <p>Phasellus quis mi quis est placerat bibendum. Pellentesque a pretium lacus, at aliquam nisi. Cras et arcu eu metus blandit auctor ultricies quis lorem. Morbi adipiscing ligula in imperdiet varius. Suspendisse nunc lacus, sollicitudin a nulla ut, molestie bibendum elit. Curabitur sed ante a ipsum convallis eleifend venenatis non orci. Suspendisse mi dui, suscipit vel lacus et, vulputate luctus felis. Maecenas sed gravida leo. In hac habitasse platea dictumst.</p>
    <p>Nullam placerat varius odio, in hendrerit sem dignissim laoreet. In dapibus non erat id vestibulum. Mauris sed quam nec erat ullamcorper tempor nec quis ligula. Duis vel iaculis justo. Phasellus et leo tempus, consequat lectus non, vestibulum risus.</p>
  </div>
  <div class="abs newsletter">
    <div class="abs newsletter-head">
      <svg width="26" height="19" viewBox="0 0 26 19"><rect x="1" y="1" width="24" height="17" fill="#fff"/><polyline points="1,1 13,11 25,1" fill="none" stroke="#2aae5e" stroke-width="2"/></svg>
      <span>Subscribe to our newsletter</span>
    </div>
    <div class="abs newsletter-input">Enter your email address</div>
    <div class="abs newsletter-button">Subscribe</div>
  </div>
</footer>

</body>
</html>
```